New business card for civil engineering company - "Keystone Audit"

We need a business card designed for our new structural engineering company.

The company name is "Keystone Audit" logo files attached.

We would like the following:
* Two-sided card
* Simple design

Information to be placed on the card:
Name - Marcus Dellow
Job Title - Director / Structural Engineer
Credentials - BEng(Hons), CPEng, CMengNZ, IntPE(NZ)
Email - marcus.dellow@keystoneaudit.co.nz
mobile - 0219364058
website - www.keystoneaudit.co.nz

```html
<!DOCTYPE html>
<html lang="en">
<head>
<meta charset="utf-8">
<title>Keystone Audit — Business Card</title>
<link rel="stylesheet" href="https://fonts.googleapis.com/css2?family=Montserrat:wght@400;500;600&display=swap">
<style>
  :root {
    --stage: #7c7d82;
    --card-front: #39393c;
    --card-back: #0a4474;
    --accent: #2aa8e0;
    --accent-text: #3a9fd9;
    --white: #ffffff;
    --muted: #8a8c92;
    --muted-back: #7f9cbc;
    --edge: #8e8f93;
  }
  * { margin: 0; padding: 0; box-sizing: border-box; }
  html, body {
    width: 1200px; height: 1200px; overflow: hidden;
    background: var(--stage);
    font-family: "Montserrat", sans-serif;
  }
  .card {
    position: absolute; top: 201px;
    width: 456px; height: 798px;
    overflow: hidden;
  }
  .card--front { left: 94px; background: var(--card-front); }
  .card--back  { left: 647px; background: var(--card-back); }

  .line { position: absolute; left: 0; width: 100%; text-align: center; white-space: nowrap; }

  .wordmark { font-weight: 600; color: var(--white); letter-spacing: 3px; }
  .tagline  { font-weight: 500; letter-spacing: 4px; }

  .card--front .wordmark { top: 316px; font-size: 33px; }
  .card--front .tagline  { top: 365px; font-size: 13px; color: var(--muted); }

  .divider {
    position: absolute; top: 436px; left: 208px;
    width: 40px; height: 2px; background: var(--accent);
  }

  .person-name { top: 486px; font-size: 23px; color: var(--accent-text); font-weight: 400; }
  .job-title   { top: 515px; font-size: 18px; color: var(--white); }
  .credentials { top: 540px; font-size: 18px; color: var(--accent-text); }

  .contact-icons {
    position: absolute; top: 597px; left: 0; width: 100%;
    display: flex; justify-content: center; gap: 14px;
  }
  .contact-icons svg { width: 20px; height: 20px; }

  .contact { font-size: 19px; color: var(--white); }
  .contact--phone { top: 653px; }
  .contact--email { top: 682px; font-size: 18px; }
  .contact--web   { top: 711px; }
  .contact--web .highlight { color: var(--accent-text); }

  .card--back .wordmark { top: 523px; font-size: 38px; }
  .card--back .tagline  { top: 580px; font-size: 16px; color: var(--muted-back); }

  .card-foot { position: absolute; left: 0; bottom: 0; width: 100%; height: 16px; }
</style>
</head>
<body>

<section class="card card--front" aria-label="Business card front">
  <div class="line wordmark">KEYSTONE AUDIT</div>
  <div class="line tagline">PEER REVIEW SPECIALISTS</div>

  <div class="divider"></div>

  <div class="line person-name">MARCUS DELLOW</div>
  <div class="line job-title">Director / Structural Engineer</div>
  <div class="line credentials">BEng(Hons), CPEng, CMengNZ, IntPE(NZ)</div>

  <div class="contact-icons" aria-hidden="true">
    <svg viewBox="0 0 20 20" fill="none" stroke="#fff" stroke-width="1.6">
      <rect x="6" y="2" width="8" height="16" rx="1.5"/>
      <line x1="9" y1="15" x2="11" y2="15"/>
    </svg>
    <svg viewBox="0 0 20 20" fill="none" stroke="#fff" stroke-width="1.4">
      <rect x="2" y="5" width="16" height="11" rx="1"/>
      <polyline points="2,5 10,11 18,5"/>
    </svg>
    <svg viewBox="0 0 20 20" fill="none" stroke="#fff" stroke-width="1.3">
      <circle cx="10" cy="10" r="8"/>
      <ellipse cx="10" cy="10" rx="3.5" ry="8"/>
      <line x1="2" y1="10" x2="18" y2="10"/>
      <line x1="3.5" y1="6" x2="16.5" y2="6"/>
      <line x1="3.5" y1="14" x2="16.5" y2="14"/>
    </svg>
  </div>

  <div class="line contact contact--phone">0219 364 058</div>
  <div class="line contact contact--email">marcus.dellow@keystoneaudit.co.nz</div>
  <div class="line contact contact--web">www.<span class="highlight">keystoneaudit</span>.co.nz</div>

  <svg class="card-foot" viewBox="0 0 456 16" preserveAspectRatio="none" aria-hidden="true">
    <rect x="0" y="10" width="456" height="6" fill="var(--edge)"/>
    <polygon points="100,16 114,2 344,2 360,16" fill="var(--accent)"/>
  </svg>
</section>

<section class="card card--back" aria-label="Business card back">
  <div class="line wordmark">KEYSTONE AUDIT</div>
  <div class="line tagline">PEER REVIEW SPECIALISTS</div>

  <svg class="card-foot" viewBox="0 0 456 16" preserveAspectRatio="none" aria-hidden="true">
    <rect x="0" y="10" width="456" height="6" fill="var(--edge)"/>
    <polygon points="94,16 108,2 343,2 358,16" fill="var(--accent)"/>
  </svg>
</section>

</body>
</html>
```